Chocolate Chip Cupcake package design

The cake is a branded packaged cupcake with chocolate chips on top and moist vanilla cake.

Our company is a baking company based in Middle East, producing high quality, European standard food snacks at an affordable price. We want a Clean, Modern and Trendy design - not too cluttered, colored yet not very busy, with a cupcake image (See attached for reference images).

Attached is Lindmoor Cupcake image - we feel it is clean but classic (we would like something more modern - this image is for your reference only, not as a guideline).

The Front side is 90 x 70mm. It will be a metallic packaging.

Target Market(s)

Teenagers, Adults - Lower, Middle and Upper Middle Class

Industry/Entity Type

It Company

Colors

Designer to choose colors to be used in the design.

Requirements
Must have
• Clean and a Modern - Appealing look
• "Choco Chip Cupcake" - product name
• Product photo
Should not have
• Too cluttered, busy background, very playful design.

```html
<!DOCTYPE html>
<html lang="en">
<head>
<meta charset="UTF-8">
<title>Muffin – Oatmeal Chocolate Chip Package Front</title>
<link href="https://fonts.googleapis.com/css2?family=Kalam:wght@700&family=Alegreya:wght@500;700&display=swap" rel="stylesheet">
<style>
  :root {
    --backdrop: #8a5a36;
    --cocoa-dark: #3e2418;
    --cocoa: #54321f;
    --cocoa-light: #7a4d30;
    --caramel: #a8754b;
    --cream: #ffffff;
    --crumb-light: #e8c990;
    --crumb-deep: #b87a3a;
    --tray-grey: #2f343a;
  }
  * { margin: 0; padding: 0; box-sizing: border-box; }
  html, body {
    width: 900px;
    height: 1200px;
    overflow: hidden;
  }
  body {
    background: var(--backdrop);
    position: relative;
    font-family: "Alegreya", Georgia, serif;
  }
  .package-front {
    position: absolute;
    left: 147px;
    top: 151px;
    width: 606px;
    height: 896px;
    overflow: hidden;
  }
  .package-art {
    position: absolute;
    inset: 0;
    width: 100%;
    height: 100%;
  }
  .product-title {
    position: absolute;
    top: 62px;
    left: 0;
    width: 100%;
    text-align: center;
    font-family: "Kalam", "Comic Sans MS", cursive;
    font-weight: 700;
    font-size: 150px;
    line-height: 1;
    color: var(--cream);
    letter-spacing: -2px;
    transform: rotate(-3deg);
  }
  .flavour-banner {
    position: absolute;
    top: 229px;
    left: 117px;
    width: 368px;
    height: 52px;
    display: flex;
    align-items: center;
    justify-content: center;
    font-size: 31px;
    font-weight: 500;
    color: var(--cocoa-dark);
    transform: rotate(1.5deg);
  }
  .trans-fat-tag {
    position: absolute;
    top: 760px;
    left: 410px;
    width: 196px;
    height: 56px;
    display: flex;
    align-items: center;
    justify-content: center;
    font-size: 30px;
    font-weight: 500;
    color: var(--cream);
    transform: rotate(9deg);
    padding-left: 14px;
  }
</style>
</head>
<body>
  <main class="package-front">
    <svg class="package-art" viewBox="0 0 606 896" xmlns="http://www.w3.org/2000/svg">
      <defs>
        <linearGradient id="cocoaPanel" x1="0" y1="0" x2="0" y2="1">
          <stop offset="0" stop-color="var(--cocoa)"/>
          <stop offset="1" stop-color="var(--cocoa-dark)"/>
        </linearGradient>
        <radialGradient id="productPhoto" cx="0.5" cy="0.55" r="0.6">
          <stop offset="0" stop-color="var(--crumb-light)"/>
          <stop offset="0.55" stop-color="var(--crumb-deep)"/>
          <stop offset="1" stop-color="var(--tray-grey)"/>
        </radialGradient>
      </defs>

      <rect class="cocoa-panel" width="606" height="896" fill="url(#cocoaPanel)"/>

      <!-- swoosh bands above the product window -->
      <path class="swoosh-band" d="M0 470 C140 360 330 330 606 380 L606 395 C330 350 150 380 0 500 Z" fill="var(--cocoa-light)" opacity="0.55"/>
      <path class="swoosh-band" d="M0 505 C150 395 330 365 606 405 L606 420 C330 385 160 420 0 530 Z" fill="var(--caramel)" opacity="0.7"/>

      <!-- product window -->
      <path class="product-window" role="img" aria-label="Photo of a golden chocolate chip muffin in a paper case on a white napkin"
            d="M0 545 C150 430 330 395 606 430 L606 896 L0 896 Z" fill="url(#productPhoto)"/>

      <!-- flavour banner shape -->
      <path class="banner-shape" d="M117 232 L485 224 L478 250 L487 276 L120 284 L127 258 Z" fill="var(--cream)"/>

      <!-- trans fat tag shape -->
      <path class="tag-shape" d="M420 752 L606 770 L606 838 L408 818 L425 788 Z" fill="var(--cocoa-dark)"/>
    </svg>

    <h1 class="product-title">Muffin</h1>
    <p class="flavour-banner">Oatmeal Chocolate Chip</p>
    <p class="trans-fat-tag">0 trans fat</p>
  </main>
</body>
</html>
```